Lotus Ember menu projecting our true authentic nature

We need a take out menu that is inviting and expresses the authentic nature of our Thai food. Also something that expresses the Thai culture. We have attached a current menu that is in need of updating. This take out menu should be something that says to potential customers "this is where I need to go." While we are Asian in nature we are specifically Thai and need to have a project that projects the Thai culture not simply Asian.

Target Market(s)

Locals and interstate traveers, college nearby, hospital personnel, mid 20s to 60s.

Industry/Entity Type

Asian Restaurant

Colors

Designer to choose colors to be used in the design.

Requirements
Must have
• Elegant, attractive features that enhance the Thai culture and provides a bit of an upscale look and appeal but that also says not overpriced for the more economical.

```html
<!DOCTYPE html>
<html lang="en">
<head>
<meta charset="utf-8">
<title>Lotus Ember Take Out Menu</title>
<link href="https://fonts.googleapis.com/css2?family=Lobster+Two:ital,wght@1,700&family=Roboto+Condensed:ital,wght@0,400;0,700;1,400&display=swap" rel="stylesheet">
<style>
:root{
  --page:#e9e6e1;
  --board:#1d1c1b;
  --board-edge:#141312;
  --ink:#f2efe9;
  --muted:#cfcac2;
  --green:#2f9a43;
  --red:#c4362b;
  --gold:#e9b22b;
  --mat:#6a4a2c;
  --plate:#eeeae3;
  --band:#b72c24;
}
*{margin:0;padding:0;box-sizing:border-box}
html,body{width:1200px;height:1000px;overflow:hidden;background:var(--page)}
body{font-family:"Roboto Condensed",Arial,sans-serif;color:var(--ink)}
.menu{position:absolute;left:35px;top:112px;width:1130px;height:730px;background:linear-gradient(180deg,#232120,var(--board) 40%,var(--board-edge));overflow:hidden}
.photo{position:absolute}
.produce-strip{left:0;top:0;width:1130px;height:32px;background:linear-gradient(90deg,#2a3a22,#4a2a1e 30%,#3b2b1c 60%,#22301f)}
.mat{background:var(--mat);opacity:.8}
.plate{border-radius:50%;background:radial-gradient(circle,#c98a3d 0 40%,var(--plate) 42%)}
.plate.wings{background:radial-gradient(ellipse,#7a3b1c 0 55%,var(--plate) 57%)}
.plate.noodles{background:radial-gradient(ellipse,#c9894b 0 58%,var(--plate) 60%)}
.coconut{border-radius:50%;background:radial-gradient(circle at 40% 40%,#8a5b33,#3a2415)}
.section{position:absolute}
h2{font-family:"Lobster Two",Georgia,cursive;font-style:italic;font-weight:700;font-size:19px;line-height:22px;margin-bottom:3px}
h2.green{color:var(--green)}
h2.red{color:var(--red)}
.row{display:flex;align-items:baseline;font-size:10px;line-height:12px;white-space:nowrap}
.row .dots{flex:1;border-bottom:1px dotted var(--muted);margin:0 2px;transform:translateY(-2px)}
.row.gold{color:var(--gold)}
.row.sub{padding-left:10px}
.desc{font-size:7.6px;line-height:9px;font-style:italic;color:var(--muted);padding-left:12px;margin-bottom:1px}
.intro{font-size:9px;line-height:11px;font-style:italic;color:var(--ink);margin-bottom:4px}
.note{font-size:7.5px;font-style:italic;color:var(--muted);text-align:right;margin-top:8px}
.chili{display:inline-block;width:16px;height:8px;vertical-align:middle;margin:0 2px}
.band{position:absolute;left:0;top:703px;width:1130px;height:18px;background:var(--band)}
.band-strip{position:absolute;left:100px;top:2px;width:930px;height:14px;background:#f4f1ec;display:flex;align-items:center;justify-content:space-around;font-size:8.5px;font-style:italic;font-weight:700;color:var(--red)}
</style>
</head>
<body>
<main class="menu">
  <div class="photo produce-strip" role="img" aria-label="Fresh vegetables, tomatoes and garlic along the top edge"></div>
  <div class="photo mat" style="left:360px;top:130px;width:140px;height:140px;transform:rotate(-25deg)" role="img" aria-label="Woven bamboo placemat"></div>
  <div class="photo mat" style="left:335px;top:270px;width:150px;height:120px;transform:rotate(-25deg)" role="img" aria-label="Woven bamboo placemat"></div>
  <div class="photo mat" style="left:890px;top:20px;width:110px;height:110px;transform:rotate(-30deg)" role="img" aria-label="Woven bamboo placemat"></div>
  <div class="photo plate" style="left:368px;top:40px;width:160px;height:115px" role="img" aria-label="Plate of fried spring rolls with sweet chili sauce"></div>
  <div class="photo plate" style="left:265px;top:163px;width:170px;height:110px" role="img" aria-label="Plate of shrimp rolls with dipping sauce"></div>
  <div class="photo plate wings" style="left:298px;top:308px;width:207px;height:150px" role="img" aria-label="Plate of Thai style chicken wings"></div>
  <div class="photo plate noodles" style="left:968px;top:0;width:162px;height:150px" role="img" aria-label="Plate of pad thai with shrimp and bean sprouts"></div>
  <div class="photo coconut" style="left:985px;top:610px;width:120px;height:95px" role="img" aria-label="Halved coconuts"></div>

  <svg width="0" height="0" style="position:absolute">
    <defs><symbol id="chili" viewBox="0 0 16 8"><path d="M1 5 Q6 8 13 3 Q14 2 15 1 L15.5 2 Q14 4 12 5 Q6 8 1 5Z" fill="#c4362b"/><path d="M13 3 L15 0.5" stroke="#3f8a36" stroke-width="1.2"/></symbol></defs>
  </svg>

  <section class="section" style="left:20px;top:30px">
    <h2 class="green">Appetizers</h2>
    <div class="row gold" style="width:345px"><span>1. Fried Springs Rolls</span><span class="dots"></span><span>(2)1.79 (4) 3.59 (6) 4.89 (12) 8.99</span></div>
    <div class="desc">Rice Wrapper Filled with Cabbage, Carrot, Bean Thread Noodles Rolled &amp; Deep Fried</div>
    <div class="row" style="width:345px"><span>2. Fresh Spring Rolls</span><span class="dots"></span><span>(2) 5.49</span></div>
    <div class="desc">Soft Rice Wrapper Filled with an Array of Shrimp, Beef, Fresh Vegetable Served with<br>Pineapple or Peanut Sauce (Both add 99¢)</div>
    <div class="row gold" style="width:300px"><span>3a.Fried Cheese Wontons</span><span class="dots"></span><span>(6) 3.49 (12) 5.89</span></div>
    <div class="desc">Thin Pastry Stuffed with Seasoned Cream Cheese Mixture &amp; Deep-Fried</div>
    <div class="row sub" style="width:260px"><span>b.Fried Wontons Variety Pak</span><span class="dots"></span><span>(12) 6.39</span></div>
    <div class="desc">6 Fried Cheese Wontons &amp; Fried Chicken Wontons</div>
    <div class="row" style="width:285px"><span>4. Fried Chicken Wontons</span><span class="dots"></span><span>(6) 4.29 (12) 6.79</span></div>
    <div class="desc">Thin Pastry Stuffed with Thin Layer of Seasoned Ground Chicken<br>&amp; Fried to a Golden Crisp</div>
    <div class="row" style="width:250px"><span>5. Spicy Meatballs</span><span class="dots"></span><span>(6) 3.99 (12) 6.79</span></div>
    <div class="desc">Seasoned Meatballs Tossed in Our Sweet &amp; Spicy<br>House Sauce</div>
    <div class="row" style="width:225px"><span>6. Tofu Todd</span><span class="dots"></span><span>4.99</span></div>
    <div class="desc">Crispy Fried Tofu Served with Our House Sweet &amp; Spicy<br>Sauce &amp; Ground Peanuts</div>
    <div class="row" style="width:235px"><span>7. Satay Kai (Chicken Satay)</span><span class="dots"></span><span>6.99</span></div>
    <div class="desc">Succulent Skewered Strips of Marinated Chicken Breast<br>Pan Seared, Served with Our Homemade Peanut Sauce<br>&amp; Cucumber Sauce</div>
    <div class="row" style="width:230px"><span>8. Shrimp Rolls</span><span class="dots"></span><span>(3) 4.99 (6) 9.79</span></div>
    <div class="desc">Jumbo Shrimp Lightly Seasoned, Wrapped<br>in a Thin Pastry then Deep-Fried to Perfection</div>
    <div class="row" style="width:230px"><span>9a.Thai Style Chicken Wings</span></div>
    <div class="row" style="width:230px"><span class="dots"></span><span>(5) 4.79 (10) 8.99 (20)16.49</span></div>
    <div class="desc">Our Special Marinated Chicken Wings are<br>Deep Fried until Golden Crisp then Tossed in<br>Our Sweet Spicy House Sauce</div>
    <div class="row sub" style="width:230px"><span>b.Fried Chicken Wings</span></div>
    <div class="row" style="width:250px"><span class="dots"></span><span>(5) 4.79 (10) 8.99 (20)16.49</span></div>
    <div class="row gold sub" style="width:265px;margin-top:4px"><span>c.Thai Sampler</span><span class="dots"></span><span>11.99</span></div>
    <div class="desc">Fried Spring Rolls, Cheese Wontons, Spicy Meatballs &amp; Wings</div>
  </section>

  <section class="section" style="left:20px;top:460px;width:350px">
    <h2 class="red">Fried Rice</h2>
    <div class="intro">Steamed Rice Stir-Fried with Our Special Thai Sauce, Carrots &amp; Onions.<br>Add Pineapple 99¢ &nbsp; Add Spring Rolls (2) 1.79 (4) 3.59</div>
    <div class="row"><span>10a. Beef Fried Rice*</span><span class="dots"></span><span>8.99 &nbsp;Thai Style</span><span class="dots"></span><span>8.99</span></div>
    <div class="row sub"><span>b. Chicken/ Roast Pork/ Pork</span><span class="dots"></span><span>7.99 &nbsp;Thai Style</span><span class="dots"></span><span>8.99</span></div>
    <div class="row sub"><span>c. Vegetarian <i style="font-size:8px">(Tofu on Request)</i></span><span class="dots"></span><span>Thai Style</span><span class="dots"></span><span>8.99</span></div>
    <div class="row sub"><span>d. Pineapple Fried Rice</span><span class="dots"></span><span>9.29 &nbsp;Thai Style</span><span class="dots"></span><span>10.29</span></div>
    <div class="desc">Steamed Rice Stir Fried with special Thai Sauce, Chicken, Chunks of Pineapple,<br>Raisins, Cashew, Carrots, Onions</div>
    <div class="row sub"><span>e. Shrimp Pineapple Fried Rice</span><span class="dots"></span><span>9.99 &nbsp;Thai Style</span><span class="dots"></span><span>10.99</span></div>
    <div class="desc">Steamed Rice Stir Fried with special Thai Sauce, Chicken, Chunks of Pineapple,<br>Raisins, Cashew, Carrots, Onions</div>
    <div class="row"><span>11.Shrimp Fried Rice</span><span class="dots"></span><span>8.69 &nbsp;Thai Style</span><span class="dots"></span><span>9.69</span></div>
    <div class="row gold"><span>12.House Fried Rice</span><span class="dots"></span><span>9.99 &nbsp;Thai Style</span><span class="dots"></span><span>10.99</span></div>
    <div class="desc">Steamed Rice Stir Fried with Chicken, Beef, Shrimp, Our Special Thai Sauce, Carrots<br>&amp; Onions</div>
    <div class="note">*Thai Style (Egg, Broccoli, Tomato, Carrot &amp; Cucumber On The Side)</div>
  </section>

  <section class="section" style="left:548px;top:30px;width:210px">
    <h2 class="red">Thai Salads</h2>
    <div class="intro">All Salads Tossed in Our Special Spicy,<br>Lemony Dressing &amp; Steam Rice</div>
    <div class="row gold" style="margin-top:8px"><span>13.Yum Nuer</span><svg class="chili"><use href="#chili"/></svg><span class="dots"></span><span>9.49</span></div>
    <div class="desc">Sliced BBQ Beef with Lettuce, Cucumbers &amp;<br>Red Onions</div>
    <div class="row"><span>14.Yum Pla Muk</span><svg class="chili"><use href="#chili"/></svg><span class="dots"></span><span>12.49</span></div>
    <div class="desc">Fresh Cooked Squid, Mixed in a Blend of<br>Lemongrass, Red Onions &amp; Thai Chili Paste<br>Served on a Bed of Lettuce</div>
    <div class="row" style="padding-left:50px"><span>15.Pla Koong</span><svg class="chili"><use href="#chili"/></svg><span class="dots"></span><span>12.49</span></div>
    <div class="desc" style="padding-left:60px">Large Shrimp Mixed in a Blend<br>of Lemongrass, Red Onions &amp;<br>Thai Chili Paste Served on a<br>Bed of Lettuce</div>
    <div class="row" style="padding-left:50px"><span>16.Yum Woon Sen</span><svg class="chili"><use href="#chili"/></svg><span class="dots"></span><span>9.49</span></div>
    <div class="desc" style="padding-left:30px">Ground Chicken &amp; Shrimp with Bean<br>Thread Noodle, Celery &amp; Onions</div>
  </section>

  <section class="section" style="left:513px;top:280px;width:245px">
    <h2 class="green" style="padding-left:35px">Soups</h2>
    <div class="row" style="padding-left:30px"><span>17.Kang Jued Woon Sen</span><span class="dots"></span><span>8.49</span></div>
    <div class="desc" style="padding-left:36px">Ground Pork, Glass Noodles, Napa Cabbage,<br>Mushrooms &amp; Green onions in a Clear Broth, Topped<br>with Cilantro</div>
    <div class="row" style="padding-left:20px"><span>18. Tom Yum Koong</span><svg class="chili"><use href="#chili"/></svg><span class="dots"></span><span>10.99</span></div>
    <div class="desc" style="padding-left:2px">Lemongrass Soup with Hot/ Sour Shrimp, Mushrooms,<br>Tomatoes &amp; Lemon Juice</div>
    <div class="row" style="padding-left:20px"><span>19. Tom Yum Gai</span><svg class="chili"><use href="#chili"/></svg><span class="dots"></span><span>8.49</span></div>
    <div class="desc" style="padding-left:2px">Lemongrass Soup with Hot/ Sour Chicken, Mushrooms,<br>Tomatoes &amp; Lemon Juice</div>
    <div class="row gold" style="padding-left:2px"><span>20.Tom Kha Gai</span><svg class="chili"><use href="#chili"/></svg><span class="dots"></span><span>9.99</span></div>
    <div class="desc" style="padding-left:2px">Lemongrass Soup with Hot/ Sour Chicken, Mushrooms,<br>Tomatoes, Coconut Milk, Galangal &amp; Lemon Juice</div>
    <div class="row" style="padding-left:2px"><span>21.Tom Kha Koong</span><svg class="chili"><use href="#chili"/></svg><span class="dots"></span><span>11.99</span></div>
    <div class="desc" style="padding-left:2px">Lemongrass Soup with Hot/ Sour Shrimp, Mushrooms, Tomatoes,<br>Coconut Milk, Galangal &amp; Lemon Juice</div>
  </section>

  <section class="section" style="left:420px;top:490px;width:338px">
    <div class="row"><span>22.Khao tom (Rice Soup) &nbsp; Chicken</span><span class="dots"></span><span>8.49 &nbsp;Shrimp</span><span class="dots"></span><span>11.49</span></div>
    <div class="desc" style="padding-left:0">Steamed Rice with Choice of Meat, Fresh Celery, Garlic &amp; Cilantro</div>
    <div class="row"><span>23.Tofu Soup</span><span class="dots"></span><span>8.49</span></div>
    <div class="desc">Tofu, Cilantro, Bean Thread Noodles &amp; Chinese Cabbage</div>
  </section>

  <section class="section" style="left:390px;top:548px;width:368px">
    <h2 class="green">Kid's Meal</h2>
    <div class="intro">All Kid's Meals Served with Fries or Rice (Steamed or Fried)</div>
    <div class="row"><span>24.Chicken Nuggets (5) / Corn Dogs (1)</span><span class="dots"></span><span>3.99</span></div>
    <div class="row"><span>25.Chicken Nuggets (9) / Corn Dogs (2)</span><span class="dots"></span><span>4.99</span></div>
  </section>

  <section class="section" style="left:390px;top:626px;width:368px">
    <h2 class="red">Salad</h2>
    <div class="row"><span>26.House Salad</span><span class="dots"></span><span>4.29 &nbsp; With Meat</span><span class="dots"></span><span>2.89</span></div>
    <div class="desc" style="padding-left:0">Choice of Dressing: Thai, Ranch, Italian, Honey Mustard, Thousand Island</div>
  </section>

  <section class="section" style="left:768px;top:30px;width:342px">
    <h2 class="green">Thai Noodles</h2>
    <div class="row" style="width:170px"><span>Chicken/ Pork/ Tofu/</span></div>
    <div class="row" style="width:165px"><span>Vegetarian</span><span class="dots"></span><span>9.29</span></div>
    <div class="row" style="width:175px"><span>Beef</span><span class="dots"></span><span>9.99</span></div>
    <div class="row" style="width:190px"><span>Shrimp or Squid</span><span class="dots"></span><span>12.69</span></div>
    <div class="row" style="width:190px;margin-bottom:12px"><span>House</span><span class="dots"></span><span>12.69</span></div>
    <div class="row"><span>27.Pad Kee Mow (Drunke Noodle)</span></div>
    <div class="desc">Stir-Fried with Wide Rice Noodles, Egg, Vegetables &amp; Thai Basil</div>
    <div class="row gold"><span>28.Pad Thai</span></div>
    <div class="desc">Thin Noodle with Bean Sprouts, Egg, Stir-fried in Sweet &amp; Sour Sauce &amp; Topped with<br>Ground Peanuts <b>(Let Your Server Know if You Have an Allergy to Peanuts)</b></div>
    <div class="row"><span>29.Mee Grob</span></div>
    <div class="desc">Crispy Egg Noodles Topped with Chinese Vegetables in Gravy</div>
    <div class="row"><span>30.Kway Teaw Lad Nar</span></div>
    <div class="desc">Stir-Fried with Broccoli &amp; Carrot in a Thai Soy Sauce Gravy Over a Bed of Wide Rice<br>Noodles</div>
    <div class="row gold"><span>31.Pad See Ew</span></div>
    <div class="desc">Stir-Fried with Egg, Broccoli &amp; Noodles</div>
    <div class="row"><span>32.Lad Nar Ta Lay</span><span class="dots"></span><span>13.99</span></div>
    <div class="desc">Shrimp, Squid, Rice Noodles, Broccoli &amp; Thai Gravy</div>
  </section>

  <section class="section" style="left:768px;top:315px;width:342px">
    <h2 class="red">Thai Noodles Soups</h2>
    <div class="row"><span>33.Beef Noodle Soup</span><span class="dots"></span><span>8.99</span></div>
    <div class="desc">Beef with Rice noodles, Bean Sprouts &amp; Green Onion</div>
    <div class="row"><span>34.Pork Noodle Soup</span><span class="dots"></span><span>7.99</span></div>
    <div class="desc">Pork with Rice noodles, Bean Sprouts, Green Onion &amp; Cilantro</div>
    <div class="row"><span>35.Roast Pork Noodle Soup</span><span class="dots"></span><span>7.99</span></div>
    <div class="desc">Roast Pork with Rice Noodles, Bean Sprouts, Green Onion &amp; Cilantro</div>
    <div class="row"><span>36.Wonton Soup</span><span class="dots"></span><span>7.99</span></div>
    <div class="desc">Thai Style with Roast Pork</div>
  </section>

  <section class="section" style="left:768px;top:452px;width:342px">
    <h2 class="green">Thai Curries</h2>
    <div style="display:flex;gap:20px">
      <div style="flex:1.6">
        <div class="row"><span>Chicken/ Pork/ Tofu/ Vegetarian</span><span class="dots"></span><span>9.49</span></div>
        <div class="row"><span>Shrimp or Squid</span><span class="dots"></span><span>12.99</span></div>
      </div>
      <div style="flex:1">
        <div class="row"><span>Beef</span><span class="dots"></span><span>10.49</span></div>
        <div class="row"><span>House</span><span class="dots"></span><span>12.99</span></div>
      </div>
    </div>
    <div class="row gold" style="margin-top:8px"><span>37.Gang Ped (Red Curry)</span><svg class="chili"><use href="#chili"/></svg></div>
    <div class="desc">Thai Spices Blended with Red Curry Paste and Rich Coconut Milk with Bamboo &amp;<br>Topped with Green &amp; Red Bell Peppers and Thai Basil</div>
    <div class="row"><span>38a.Gang Khew Whan (Green Curry)</span><svg class="chili"><use href="#chili"/></svg></div>
    <div class="desc">Thai Spices Blended with Green Curry Paste and Rich Coconut Milk with Bamboo &amp;<br>Topped with Green &amp; Red Bell Peppers and Thai Basil</div>
    <div class="row sub"><span>b.Gang Karee (Yellow Curry)</span><svg class="chili"><use href="#chili"/></svg></div>
    <div class="desc">Thai Spices Blended with Yellow Curry Paste and Rich Coconut Milk<br>with Potatoes, Carrots &amp; Onions</div>
    <div class="row sub"><span>c.Gang Karee (Yellow Curry)</span><svg class="chili"><use href="#chili"/></svg></div>
    <div class="desc">Massaman, Mildest of All Curries, is Creamy &amp;<br>Blended with Potatoes, Carrot, Onion &amp; Peanut</div>
    <div class="row"><span>39.Panang Curry</span><svg class="chili"><use href="#chili"/></svg></div>
    <div class="desc">Sweet Red Curry Blended in Rich Coconut Milk</div>
  </section>

  <footer class="band">
    <div class="band-strip">
      <span><svg class="chili"><use href="#chili"/></svg> INDICATES ITEM ARE SPICY. PLEASE INDICATE LEVEL OF SPICYNESS</span>
      <span><svg class="chili"><use href="#chili"/></svg> Choice of Mild</span>
      <span><svg class="chili"><use href="#chili"/></svg><svg class="chili"><use href="#chili"/></svg> Medium</span>
      <span><svg class="chili"><use href="#chili"/></svg><svg class="chili"><use href="#chili"/></svg><svg class="chili"><use href="#chili"/></svg> Hot</span>
      <span><svg class="chili"><use href="#chili"/></svg><svg class="chili"><use href="#chili"/></svg><svg class="chili"><use href="#chili"/></svg><svg class="chili"><use href="#chili"/></svg> Thai Hot</span>
    </div>
  </footer>
</main>
</body>
</html>
```